Business Card Design for an Investment Company

We need a business card design for our private investment company, called Ashbourne Partners. Ashbourne Partners is an investments partnership that aims to acquire shares in listed companies with a view to influencing those companies through active dialogue in order to improve their value. We need designs that use the logo colors (blue, grey, white), we need both English and Arabic on the business cards (can be on one side or 2 sides). The final logo should communicate professionalism, conservatism (nothing too fancy or too cheesy), that we are smart, conservative and old school.

Target Market(s)

Investment companies

Industry/Entity Type

Investment

Contact Information for Business Card

Khalid Yousef Rumaithi
Senior Executive Officer

Palm Terrace 07, Level 3, Office 215/12
HLMZ

+9714987650
krumaithi@ashbournepartners.com
www.ashbournepartners.com

Requirements
Must have
• Logo to be placed on the left hand side of the business card
• for the Arabic, we only need to have the name and title so it can be accomodated on one side so we can have the other side with full color and logo. The arabic that needs to be used is the below:
• خالد يوسف الرميثي
• المدير التنفيدي

```html
<!DOCTYPE html>
<html lang="en">
<head>
<meta charset="utf-8">
<title>Ashbourne Partners – Business Card</title>
<link rel="stylesheet" href="https://fonts.googleapis.com/css2?family=Roboto:wght@400;500;700&family=Noto+Sans+Arabic:wght@400&display=swap">
<style>
  :root {
    --bg: #e6e6e6;
    --brand-blue: #1a6fa3;
    --card-blue-dark: #06679c;
    --card-blue-light: #1f82b4;
    --text-grey: #555555;
    --white: #ffffff;
  }
  * { margin: 0; padding: 0; box-sizing: border-box; }
  html, body {
    width: 1200px; height: 1000px; overflow: hidden;
    background: var(--bg);
    font-family: "Roboto", Arial, sans-serif;
  }
  .card {
    position: absolute;
    left: 269px;
    width: 662px;
    box-shadow: 0 3px 8px rgba(0,0,0,0.25);
  }
  .card-front {
    top: 108px; height: 378px;
    background: linear-gradient(120deg, var(--card-blue-dark) 0%, var(--card-blue-light) 55%, var(--card-blue-dark) 100%);
    color: var(--white);
  }
  .front-wordmark {
    position: absolute; left: 0; right: 0; top: 158px;
    text-align: center;
    font-size: 46px; font-weight: 700; letter-spacing: -0.5px;
    color: var(--white);
  }
  .front-url {
    position: absolute; left: 0; right: 0; top: 330px;
    text-align: center;
    font-size: 19px; font-weight: 400;
  }
  .card-back {
    top: 521px; height: 379px;
    background: var(--white);
  }
  .back-wordmark {
    position: absolute; left: 38px; top: 36px;
    font-size: 40px; font-weight: 700; letter-spacing: -0.5px;
    color: var(--brand-blue);
  }
  .person-en { position: absolute; left: 38px; top: 190px; }
  .person-name {
    font-size: 20px; font-weight: 400; color: var(--brand-blue);
    letter-spacing: 0.2px;
  }
  .person-title { font-size: 15px; color: var(--text-grey); margin-top: 4px; }
  .person-ar {
    position: absolute; right: 37px; top: 188px;
    text-align: right; direction: rtl;
    font-family: "Noto Sans Arabic", Arial, sans-serif;
  }
  .person-ar .person-name { font-size: 19px; }
  .person-ar .person-title { font-size: 17px; margin-top: 2px; }
  .contact {
    position: absolute; left: 38px; top: 280px;
    font-size: 15px; color: var(--text-grey); line-height: 21px;
  }
  .contact-row { display: flex; align-items: center; gap: 4px; }
  .contact-row svg { width: 12px; height: 12px; fill: var(--brand-blue); }
  .address {
    position: absolute; right: 37px; top: 280px;
    text-align: right; font-size: 15px; color: var(--text-grey); line-height: 21px;
  }
</style>
</head>
<body>
  <section class="card card-front">
    <div class="front-wordmark">Ashbourne Partners</div>
    <div class="front-url">www.ashbournepartners.com</div>
  </section>

  <section class="card card-back">
    <div class="back-wordmark">Ashbourne Partners</div>

    <div class="person-en">
      <div class="person-name">Khalid Yousef Rumaithi</div>
      <div class="person-title">Senior Executive Officer</div>
    </div>

    <div class="person-ar" lang="ar">
      <div class="person-name">خالد يوسف الرميثي</div>
      <div class="person-title">المدير التنفيدي</div>
    </div>

    <div class="contact">
      <div class="contact-row">
        <svg viewBox="0 0 24 24" aria-hidden="true"><path d="M6.6 10.8a15.1 15.1 0 0 0 6.6 6.6l2.2-2.2c.3-.3.7-.4 1-.2 1.1.4 2.3.6 3.6.6.6 0 1 .4 1 1V20c0 .6-.4 1-1 1C10.6 21 3 13.4 3 4c0-.6.4-1 1-1h3.5c.6 0 1 .4 1 1 0 1.3.2 2.5.6 3.6.1.3 0 .7-.2 1z"/></svg>
        <span>+9714987650</span>
      </div>
      <div class="contact-row">
        <svg viewBox="0 0 24 24" aria-hidden="true"><path d="M2 5h20v14H2z M2 5l10 8 10-8" stroke="#fff" stroke-width="1.5"/></svg>
        <span>krumaithi@ashbournepartners.com</span>
      </div>
    </div>

    <div class="address">
      <div>Palm Terrace 07, Level 3</div>
      <div>Office 215/12</div>
      <div>HLMZ</div>
    </div>
  </section>
</body>
</html>
```